Bourbon Label Design For a Unique Craft Distillery

We are a craft distillery located in Ashford Mill PA looking for a label design for our new bourbon brand. The Name of the bourbon is going to be called "Iron Meadow" and the type of bourbon is a "straight Bourbon Whiskey". The First file are the pictures of our current brands. Would like the design to look Vintage but pop. The Bourbon will be a top shelf item. The Pictures of the other bottle are brands we like.

Target Market(s)

21-65 years old

Font styles to use
Decorative
Script

Colors
ec1f27
3176b5
1b1b1b
f5f5f5

Requirements
Must have
• vintage look, and pop !

```html
<!DOCTYPE html>
<html lang="en">
<head>
<meta charset="utf-8">
<title>Iron Meadow — Straight Bourbon Whiskey Label</title>
<link href="https://fonts.googleapis.com/css2?family=Russo+One&family=Josefin+Sans:wght@600&family=Courier+Prime&family=Oswald:wght@500&display=swap" rel="stylesheet">
<style>
  :root {
    --ink: #1b1b1b;
    --paper: #ffffff;
    --copper: #b97a4b;
    --bg-center: #ffffff;
    --bg-edge: #d9d9d9;
    --art-tone: #d4d4d4;
  }
  html, body {
    margin: 0;
    width: 1200px;
    height: 1200px;
    overflow: hidden;
  }
  body {
    background: radial-gradient(circle at 50% 50%, var(--bg-center) 35%, var(--bg-edge) 100%);
  }
  .label { display: block; width: 1200px; height: 1200px; }
  .stamp-paper { fill: var(--paper); }
  .frame-copper { fill: var(--copper); stroke: var(--ink); stroke-width: 3; }
  .frame-inner { fill: var(--paper); stroke: var(--ink); stroke-width: 3; }
  .locomotive-art { fill: var(--art-tone); }
  .rule { stroke: var(--ink); stroke-width: 4; }
  .brand-name { font-family: "Russo One", sans-serif; font-size: 98px; fill: var(--ink); }
  .spirit-type { font-family: "Josefin Sans", sans-serif; font-weight: 600; font-size: 19px; fill: var(--ink); letter-spacing: 0.5px; }
  .dot { fill: var(--ink); }
  .spec-box { fill: none; stroke: var(--ink); stroke-width: 3.5; }
  .spec-text { font-family: "Courier Prime", monospace; font-size: 19px; fill: var(--ink); }
  .dotted-line { stroke: var(--ink); stroke-width: 5; stroke-linecap: round; stroke-dasharray: 0 9; }
  .origin { font-family: "Oswald", sans-serif; font-weight: 500; font-size: 16px; fill: var(--ink); }
</style>
</head>
<body>
<svg class="label" viewBox="0 0 1200 1200" xmlns="http://www.w3.org/2000/svg">
  <defs>
    <mask id="perforation">
      <rect x="0" y="0" width="1200" height="1200" fill="#000"/>
      <rect x="271" y="192" width="660" height="816" fill="#fff"/>
      <g fill="#000">
        <circle cx="296" cy="192" r="15"/><circle cx="357" cy="192" r="15"/><circle cx="418" cy="192" r="15"/><circle cx="479" cy="192" r="15"/><circle cx="540" cy="192" r="15"/><circle cx="601" cy="192" r="15"/><circle cx="662" cy="192" r="15"/><circle cx="723" cy="192" r="15"/><circle cx="784" cy="192" r="15"/><circle cx="845" cy="192" r="15"/><circle cx="906" cy="192" r="15"/>
        <circle cx="296" cy="1008" r="15"/><circle cx="357" cy="1008" r="15"/><circle cx="418" cy="1008" r="15"/><circle cx="479" cy="1008" r="15"/><circle cx="540" cy="1008" r="15"/><circle cx="601" cy="1008" r="15"/><circle cx="662" cy="1008" r="15"/><circle cx="723" cy="1008" r="15"/><circle cx="784" cy="1008" r="15"/><circle cx="845" cy="1008" r="15"/><circle cx="906" cy="1008" r="15"/>
        <circle cx="271" cy="262" r="15"/><circle cx="271" cy="328" r="15"/><circle cx="271" cy="394" r="15"/><circle cx="271" cy="460" r="15"/><circle cx="271" cy="526" r="15"/><circle cx="271" cy="592" r="15"/><circle cx="271" cy="658" r="15"/><circle cx="271" cy="724" r="15"/><circle cx="271" cy="790" r="15"/><circle cx="271" cy="856" r="15"/><circle cx="271" cy="922" r="15"/>
        <circle cx="931" cy="262" r="15"/><circle cx="931" cy="328" r="15"/><circle cx="931" cy="394" r="15"/><circle cx="931" cy="460" r="15"/><circle cx="931" cy="526" r="15"/><circle cx="931" cy="592" r="15"/><circle cx="931" cy="658" r="15"/><circle cx="931" cy="724" r="15"/><circle cx="931" cy="790" r="15"/><circle cx="931" cy="856" r="15"/><circle cx="931" cy="922" r="15"/>
      </g>
    </mask>
  </defs>

  <g class="stamp">
    <rect class="stamp-paper" x="271" y="192" width="660" height="816" mask="url(#perforation)"/>
    <rect class="frame-copper" x="311" y="228" width="579" height="740"/>
    <rect class="frame-inner" x="326" y="243" width="549" height="710"/>
  </g>

  <rect class="locomotive-art" x="415" y="282" width="350" height="177" rx="6" role="img" aria-label="Engraved illustration of a vintage steam locomotive on rails"/>

  <g class="title-block">
    <line class="rule" x1="393" y1="508" x2="805" y2="508"/>
    <text class="brand-name" x="404" y="614" textLength="389" lengthAdjust="spacingAndGlyphs">IRON</text>
    <text class="brand-name" x="399" y="692" textLength="394" lengthAdjust="spacingAndGlyphs">MEADOW</text>
    <line class="rule" x1="393" y1="705" x2="805" y2="705"/>
    <g class="dot">
      <circle cx="397" cy="725" r="3.5"/><circle cx="408" cy="725" r="3.5"/><circle cx="419" cy="725" r="3.5"/><circle cx="430" cy="725" r="3.5"/>
      <circle cx="769" cy="725" r="3.5"/><circle cx="780" cy="725" r="3.5"/><circle cx="791" cy="725" r="3.5"/><circle cx="802" cy="725" r="3.5"/>
    </g>
    <text class="spirit-type" x="600" y="732" text-anchor="middle" textLength="315" lengthAdjust="spacingAndGlyphs">STRAIGHT BOURBON WHISKEY</text>
  </g>

  <g class="spec-table">
    <rect class="spec-box" x="356" y="777" width="120" height="110"/>
    <rect class="spec-box" x="476" y="777" width="246" height="110"/>
    <rect class="spec-box" x="722" y="777" width="120" height="110"/>
    <text class="spec-text" x="416" y="810" text-anchor="middle">VOL.</text>
    <text class="spec-text" x="416" y="853" text-anchor="middle">750 ml</text>
    <text class="spec-text" x="599" y="810" text-anchor="middle">BOTTLE BACH.</text>
    <text class="spec-text" x="782" y="810" text-anchor="middle">PROOF</text>
    <text class="spec-text" x="782" y="853" text-anchor="middle">80</text>
  </g>

  <g class="origin-line">
    <line class="dotted-line" x1="360" y1="910" x2="530" y2="910"/>
    <text class="origin" x="601" y="916" text-anchor="middle">ASHFORD MILL PA</text>
    <line class="dotted-line" x1="673" y1="910" x2="848" y2="910"/>
  </g>
</svg>
</body>
</html>
```